K P Guard Services - Alarm and CCTV installation Flyer

Need a flyer designed that grabs the attention of potential customers, we need the price to stand out the most to grab people’s attention, whether they are residential or commercial.We are a security company based in Brentwood Essex but cover London and the home counties. here is our website to take a look at www.kpguardservices.co.uk. We want them to know we install complete alarm and Cctv systems and will keep them “safe”

Target Market(s)

residential and commercial property

Colors
f37122

Requirements
Must have
• on one side
• large clear logo - professional design
• - Intruder Alarms starting from £495 + VAT. (Big text)
• - £150 discount on installations
• *terms and conditions apply (small text)
• - Not happy with your current provider? Free of charge no obligation take over survey and quotation and up to £100 off
• - CCTV systems starting from £595 + VAT (based on 2 cameras)
• K P Guard Services are always there, always available, wherever and whenever you need us.
• Large telephone number at the bottom 01632 480913
• Address / email / website as a footer * see website for details
• on second side
• large and bold
• Are you looking to keep you and your premises safe?
• - K P Guard Services install, maintain and repair all intruder alarms, CCTV, intercom and access control
• - View, control and manage your security systems anywhere in the world
• - Feel at ease with monitoring services & police response tailored to suit you and your business
• - K P Guard can takeover any existing security system and offer maintenance checks to guarantee the best performance for you and your premises
• - K P Guard understand that being security conscious is ever increasing, protecting your property and family is a number one priority
• - Our fully insured and accredited team offer quality, safety and cost efficiency throughout the whole process
• - K P Guard Services are using the latest cloud-based technology to stay connected with your home and business 24/7
• If you are looking to improve the security in your home, office or commercial property then call a member of our team today for a free quote.
• Fully insured and accredited
• Jobrater logo and NQRB Intruder and CCTV logos
• Logo somewhere on page and
• Telephone number
• Address / email / website as footer
Nice to have
• We would like to have the text saying
• Intruder alarms installed from £495 + vat the biggest text on the page. Most likely the £495 part the largest.
• Also would like “not happy with your current provider” more obvious
• We would like use our company colours - Orange/White/black

```html
<!DOCTYPE html>
<html lang="en">
<head>
<meta charset="utf-8">
<title>K P Guard Services – Alarm and CCTV Flyer</title>
<link rel="stylesheet" href="https://fonts.googleapis.com/css2?family=Oswald:wght@400;500;600;700&family=Roboto:wght@400;700;900&family=Open+Sans:ital,wght@0,400;0,600;0,700;1,400;1,700&display=swap">
<style>
:root{
  --orange:#f37122;
  --orange-deep:#e25d10;
  --brand-red:#e5322b;
  --dark:#2d2d2d;
  --darker:#262626;
  --ink:#1b1b1b;
  --light:#e9e9e9;
  --white:#ffffff;
  --stage:#a6a6a6;
}
*{box-sizing:border-box;margin:0;padding:0}
html,body{width:1200px;height:902px;overflow:hidden}
body{background:var(--stage);position:relative;font-family:"Open Sans",Arial,sans-serif}
.flyer{position:absolute;overflow:hidden;background:var(--white)}
.flyer-front{left:120px;top:145px;width:442px;height:621px}
.flyer-back{left:659px;top:187px;width:442px;height:621px}
.abs{position:absolute}
.nowrap{white-space:nowrap}

/* front */
.front-bg{left:0;top:0}
.camera-photo{left:225px;top:0;width:217px;height:250px;background:radial-gradient(circle at 50% 38%,#7a1010 0%,#3a3a3a 28%,#cfcfcf 52%,#f2f2f2 78%)}
.brand-front{left:22px;top:22px;width:200px;text-align:center}
.brand-mark{width:40px;height:40px;background:var(--brand-red);margin:0 auto 10px}
.brand-name{font-family:"Roboto",Arial,sans-serif;font-weight:700;color:var(--brand-red);font-size:23px;line-height:1.1;letter-spacing:.5px}
.headline-alarm{left:21px;top:196px;font-family:"Roboto",Arial,sans-serif;font-weight:700;color:var(--white);font-size:39px;line-height:42px;letter-spacing:-.5px;white-space:nowrap}
.starting-from{left:221px;top:196px;font-family:"Oswald",Arial,sans-serif;font-weight:500;color:var(--white);font-size:18px;line-height:22px;white-space:nowrap}
.price-alarm{left:218px;top:208px;font-family:"Oswald",Arial,sans-serif;font-weight:700;color:var(--ink);font-size:66px;line-height:80px;letter-spacing:-2px;white-space:nowrap}
.price-alarm .vat{font-size:18px;color:var(--white);letter-spacing:0;font-weight:600}
.discount-badge{left:47px;top:327px;width:148px;height:126px}
.discount-text{left:47px;top:348px;width:148px;text-align:center;font-family:"Roboto",Arial,sans-serif}
.discount-amount{font-family:"Oswald",Arial,sans-serif;font-weight:500;font-size:36px;line-height:38px;color:var(--orange)}
.discount-label{font-weight:700;font-size:17px;line-height:17px;color:var(--ink)}
.discount-sub{font-weight:700;font-size:9px;color:var(--orange)}
.discount-terms{font-family:"Open Sans",Arial,sans-serif;font-size:6.5px;color:var(--ink);margin-top:2px;line-height:8px}
.provider-question{left:235px;top:318px;font-family:"Oswald",Arial,sans-serif;font-weight:500;color:var(--white);font-size:22px;line-height:27px;white-space:nowrap}
.takeover-offer{left:235px;top:383px;width:186px;height:41px;background:var(--light);border-radius:4px}
.takeover-copy{left:5px;top:6px;width:100px;text-align:center;font-family:"Roboto",Arial,sans-serif;font-weight:700;font-size:5.2px;line-height:6.6px;color:var(--ink);white-space:nowrap}
.takeover-copy .free{display:block;font-family:"Oswald",Arial,sans-serif;font-weight:500;font-size:11px;line-height:12px;color:var(--orange)}
.takeover-amount{left:107px;top:0;font-family:"Oswald",Arial,sans-serif;font-weight:700;font-size:32px;line-height:41px;color:var(--ink);letter-spacing:-1px}
.takeover-off{left:176px;top:21px;transform:translate(-50%,-50%) rotate(-90deg);font-family:"Oswald",Arial,sans-serif;font-weight:700;font-size:13px;color:var(--orange)}
.cctv-line{left:27px;top:463px;font-family:"Roboto",Arial,sans-serif;font-weight:700;color:var(--white);font-size:15px;white-space:nowrap}
.cctv-sub{left:53px;top:485px;font-family:"Roboto",Arial,sans-serif;font-weight:700;color:var(--white);font-size:10.5px;white-space:nowrap}
.cctv-seal{left:262px;top:436px;width:92px;height:92px}
.cctv-price{left:262px;top:456px;width:92px;text-align:center;font-family:"Oswald",Arial,sans-serif;font-weight:700;font-size:38px;line-height:50px;color:var(--ink);letter-spacing:-1px}
.cctv-vat{left:361px;top:462px;font-family:"Roboto",Arial,sans-serif;font-weight:700;color:var(--white);font-size:20px;white-space:nowrap}
.call-band{left:0;top:507px;width:442px;height:68px;background:var(--light)}
.call-label{left:31px;top:530px;font-family:"Roboto",Arial,sans-serif;font-weight:900;color:var(--ink);font-size:20px;white-space:nowrap}
.call-icon{left:136px;top:527px;width:28px;height:28px}
.call-number{left:178px;top:518px;font-family:"Roboto",Arial,sans-serif;font-weight:700;color:var(--orange);font-size:36px;line-height:44px;white-space:nowrap}
.front-footer{left:0;top:575px;width:442px;height:46px;background:var(--darker)}
.contact-item{display:flex;align-items:center;gap:5px;font-family:"Open Sans",Arial,sans-serif;color:var(--white);font-size:6.5px;line-height:8px;white-space:nowrap}
.contact-dot{flex:none;width:14px;height:14px;border-radius:50%;background:var(--orange);display:flex;align-items:center;justify-content:center}

/* back */
.back-header{left:0;top:0;width:442px;height:97px;background:var(--orange)}
.header-question{left:30px;top:25px;font-family:"Oswald",Arial,sans-serif;font-weight:500;color:var(--ink);font-size:27px;line-height:32px;white-space:nowrap}
.header-sub{left:27px;top:62px;font-family:"Oswald",Arial,sans-serif;font-weight:500;color:var(--white);font-size:18.5px;line-height:24px;white-space:nowrap}
.header-safe{left:274px;top:8px;font-family:"Oswald",Arial,sans-serif;font-weight:700;color:var(--white);font-size:64px;line-height:84px;white-space:nowrap}
.keypad-photo{left:0;top:97px;width:442px;height:223px;background:linear-gradient(110deg,#c9cacc 0%,#8b8e93 25%,#e3e4e6 45%,#9aa1ab 70%,#eef0f2 100%)}
.features-panel{left:0;top:320px;width:442px;height:170px;background:var(--dark)}
.feature-list{left:22px;top:336px;width:268px;list-style:none}
.feature-list li{position:relative;padding-left:18px;font-size:6.3px;line-height:8.2px;color:var(--white);margin-bottom:5px}
.feature-list li::before{content:"";position:absolute;left:0;top:0;width:9px;height:9px;border-radius:1px;background:var(--orange)}
.feature-list li::after{content:"";position:absolute;left:2.5px;top:1.3px;width:3px;height:5px;border:solid var(--white);border-width:0 1.5px 1.5px 0;transform:rotate(40deg)}
.feature-list em{font-weight:700}
.feature-list .accent{color:var(--orange)}
.app-photo{left:300px;top:338px;width:128px;height:140px;background:linear-gradient(160deg,#1c1c1e 0%,#3a8fd0 40%,#d9e8f4 70%,#2a2a2c 100%);border-radius:10px}
.brand-back{left:8px;top:503px;width:160px;text-align:center}
.accreditations{left:196px;top:500px;display:flex;gap:8px;align-items:center}
.badge-plain{width:34px;height:34px;border:1.5px solid #9a9a9a;background:#f4f4f4}
.badge-round{width:28px;height:28px;border-radius:50%;border:1.5px solid #9a9a9a;background:#f4f4f4}
.listing-name{font-family:"Roboto",Arial,sans-serif;font-weight:700;color:var(--brand-red);font-size:18px;margin-left:6px}
.quote-note{left:183px;top:544px;width:252px;font-style:italic;font-size:6.8px;line-height:8.5px;color:var(--ink)}
.contact-strip{left:176px;top:577px;width:266px;height:39px;background:var(--orange)}
.contact-strip .contact-dot{width:11px;height:11px;background:var(--dark)}
.contact-strip .contact-item{font-size:6px;line-height:7px}
</style>
</head>
<body>

<section class="flyer flyer-front" aria-label="Flyer front">
  <div class="abs camera-photo" role="img" aria-label="Photo of a white CCTV dome camera with red infrared lights"></div>
  <svg class="abs front-bg" width="442" height="621" viewBox="0 0 442 621" aria-hidden="true">
    <polygon points="0,312 442,238 442,507 0,507" fill="#2d2d2d"/>
    <polygon points="0,186 442,124 442,238 0,312" fill="#f37122"/>
    <polygon points="0,302 442,230 442,240 0,314" fill="#e25d10"/>
  </svg>

  <div class="abs brand-front">
    <div class="brand-mark"></div>
    <div class="brand-name">K P GUARD SERVICES</div>
  </div>

  <div class="abs headline-alarm">INTRUDER<br>ALARMS</div>
  <div class="abs starting-from">STARTING FROM</div>
  <div class="abs price-alarm">£495<span class="vat"> + VAT</span></div>

  <svg class="abs discount-badge" viewBox="0 0 148 126" aria-hidden="true">
    <polygon points="74,0 148,31 148,95 74,126 0,95 0,31" fill="#e9e9e9"/>
    <polygon points="74,7 141,35 141,91 74,119 7,91 7,35" fill="none" stroke="#2d2d2d" stroke-width="1.2" stroke-dasharray="3 2"/>
  </svg>
  <div class="abs discount-text">
    <div class="discount-amount">£150</div>
    <div class="discount-label">DISCOUNT</div>
    <div class="discount-sub">ON INSTALLATIONS</div>
    <div class="discount-terms">*terms and conditions<br>apply</div>
  </div>

  <div class="abs provider-question">NOT HAPPY WITH YOUR<br>CURRENT PROVIDER?</div>
  <div class="abs takeover-offer">
    <div class="abs takeover-copy"><span class="free">FREE OF CHARGE</span>NO OBLIGATION TAKE OVER SURVEY<br>AND QUOTATION AND UP TO</div>
    <div class="abs takeover-amount">£100</div>
    <div class="abs takeover-off">OFF</div>
  </div>

  <div class="abs cctv-line">CCTV SYSTEMS STARTING FROM</div>
  <div class="abs cctv-sub">(BASED ON 2 CAMERAS)</div>

  <div class="abs call-band"></div>
  <svg class="abs cctv-seal" viewBox="0 0 92 92" aria-hidden="true">
    <defs>
      <radialGradient id="sealFill" cx="50%" cy="35%" r="65%">
        <stop offset="0" stop-color="#ffa65a"/>
        <stop offset="1" stop-color="#e25d10"/>
      </radialGradient>
    </defs>
    <circle cx="46" cy="46" r="45" fill="#bdbdbd"/>
    <circle cx="46" cy="46" r="40" fill="url(#sealFill)"/>
  </svg>
  <div class="abs cctv-price">£595</div>
  <div class="abs cctv-vat">+ VAT</div>

  <div class="abs call-label">CALL US !</div>
  <svg class="abs call-icon" viewBox="0 0 28 28" aria-hidden="true">
    <circle cx="14" cy="14" r="12.5" fill="none" stroke="#1b1b1b" stroke-width="2"/>
    <path d="M10 7.5c.8-.5 1.6-.3 2 .4l1.2 2.3c.3.6.1 1.3-.4 1.7l-.9.7c.6 1.6 1.8 2.9 3.3 3.6l.8-.9c.4-.5 1.100-.6 1.7-.3l2.2 1.3c.7.4.8 1.3.3 1.9-1.2 1.4-3 1.7-4.7.8-3.2-1.7-5.4-4.4-6.2-7.7-.3-1.5.1-3 .7-3.800z" fill="#1b1b1b"/>
  </svg>
  <div class="abs call-number">01632 480913</div>

  <footer class="abs front-footer">
    <div class="abs contact-item" style="left:23px;top:14px">
      <span class="contact-dot"><svg width="8" height="8" viewBox="0 0 10 10"><path d="M5 1 1 5h1.3v4h2V6.5h1.4V9h2V5H9z" fill="#fff"/></svg></span>
      <span>14 Meadow Lane,<br>Brentwood, Essex, CM15 2XY</span>
    </div>
    <div class="abs contact-item" style="left:159px;top:17px">
      <span class="contact-dot"><svg width="8" height="8" viewBox="0 0 10 10"><rect x="1" y="2.5" width="8" height="5.5" fill="#fff"/><path d="M1 2.5 5 6l4-3.5" fill="none" stroke="#f37122" stroke-width=".9"/></svg></span>
      <span>operations@kpguardservices.co.uk</span>
    </div>
    <div class="abs contact-item" style="left:303px;top:17px">
      <span class="contact-dot"><svg width="8" height="8" viewBox="0 0 10 10"><circle cx="5" cy="5" r="3.8" fill="none" stroke="#fff" stroke-width=".9"/><path d="M1.2 5h7.6M5 1.2c-2 2.2-2 5.4 0 7.6M5 1.2c2 2.2 2 5.4 0 7.6" fill="none" stroke="#fff" stroke-width=".8"/></svg></span>
      <span>www.kpguardservices.co.uk</span>
    </div>
  </footer>
</section>

<section class="flyer flyer-back" aria-label="Flyer back">
  <header class="abs back-header">
    <div class="abs header-question">ARE YOU LOOKING TO</div>
    <div class="abs header-sub">KEEP YOU AND YOUR PREMISES</div>
    <div class="abs header-safe">SAFE?</div>
  </header>

  <div class="abs keypad-photo" role="img" aria-label="Photo of a chrome alarm keypad with a blue display reading Welcome Home, in a modern interior"></div>

  <div class="abs features-panel"></div>
  <ul class="abs feature-list">
    <li>K P Guard Services <em>install, maintain and repair</em> all intruder alarms, CCTV, intercom and access control</li>
    <li>View, control and manage your security systems <em>anywhere in the world</em></li>
    <li>Feel at ease with monitoring services &amp; police response tailored to suit you and your business</li>
    <li>K P Guard can takeover any existing security system and offer maintenance checks to guarantee the best performance for you and your premises</li>
    <li>K P Guard understand that being security conscious is ever increasing, protecting your property and family is a number one priority</li>
    <li>Our fully insured and accredited team <em>offer quality, safety and cost efficiency</em> throughout the whole process</li>
    <li>K P Guard Services are using the latest <em>cloud-based technology</em> to stay connected with your home and business <span class="accent">24/7</span></li>
  </ul>
  <div class="abs app-photo" role="img" aria-label="Photo of two smartphones showing the security control app"></div>

  <div class="abs brand-back">
    <div class="brand-mark"></div>
    <div class="brand-name" style="font-size:20px">K P GUARD SERVICES</div>
  </div>

  <div class="abs accreditations" aria-label="Accreditations">
    <div class="badge-plain"></div>
    <div class="badge-plain"></div>
    <div class="badge-round"></div>
    <span class="listing-name">Jobrater</span>
  </div>

  <p class="abs quote-note">If you are looking to improve the security in your home, office or commercial property then call a member of our team today for a free quote.</p>

  <footer class="abs contact-strip">
    <div class="abs contact-item" style="left:6px;top:5px">
      <span class="contact-dot"></span>
      <span>14 Meadow Lane,<br>Brentwood, Essex, CM15 2XY</span>
    </div>
    <div class="abs contact-item" style="left:6px;top:24px">
      <span class="contact-dot"></span>
      <span>01632 480913</span>
    </div>
    <div class="abs contact-item" style="left:126px;top:7px">
      <span class="contact-dot"></span>
      <span>operations@kpguardservices.co.uk</span>
    </div>
    <div class="abs contact-item" style="left:126px;top:22px">
      <span class="contact-dot"></span>
      <span>www.kpguardservices.co.uk</span>
    </div>
  </footer>
</section>

</body>
</html>
```